Freshen up Product Labels

We need product label designs refreshed throughout our brand. We will start with the main product as that will set the basic design for most other labels. We are currently using 2.5" wide x 4.5" tall vinyl labels for most products and would like to stick to that size for this project. There are 3 of this size label on a jug of our all natural house cleaning concentrate. Uploaded current design and open to your new ideas. Our products can be found in more detail at voldrimo.com

```html
<!DOCTYPE html>
<html lang="en">
<head>
<meta charset="utf-8">
<title>Voldrimo Aromatherapy Cleaning Concentrate – Labels</title>
<link href="https://fonts.googleapis.com/css2?family=Cabin+Sketch:wght@700&family=Montserrat:wght@500;700&display=swap" rel="stylesheet">
<style>
  :root{
    --plum:#5c1a4a;
    --plum-deep:#4a123b;
    --leaf:#5cb84c;
    --leaf-deep:#3f9c3a;
    --lime:#a8c83a;
    --brand-green:#4cb848;
    --white:#ffffff;
    --page:#ffffff;
  }
  *{box-sizing:border-box;margin:0;padding:0}
  html,body{width:847px;height:1200px;overflow:hidden;background:var(--page)}
  .sheet{position:relative;width:847px;height:1200px;
    display:flex;justify-content:center;align-items:center;gap:34px}
  .label{position:relative;width:247px;height:444px;overflow:hidden;
    font-family:"Montserrat",Arial,sans-serif;color:var(--white);text-align:center}
  .label--plum{background:var(--plum)}
  .label--leaf{background:var(--leaf)}
  .banner{position:absolute;left:60px;top:0;width:127px;height:106px}
  .brand-name{position:absolute;left:0;right:0;top:52px;font-weight:700;font-size:19px;
    letter-spacing:1px;color:var(--brand-green)}
  .tree-art{position:absolute;left:25px;top:128px;width:200px;height:185px;border-radius:50%}
  .label--plum .tree-art{background:radial-gradient(ellipse at center,var(--plum-deep) 0%,var(--plum-deep) 45%,rgba(74,18,59,0) 72%)}
  .label--leaf .tree-art{background:radial-gradient(ellipse at center,var(--leaf-deep) 0%,var(--leaf-deep) 45%,rgba(63,156,58,0) 72%)}
  .title{position:absolute;left:0;right:0;top:136px;font-family:"Cabin Sketch",cursive;
    font-weight:700;font-size:33px;line-height:34px;letter-spacing:0.5px}
  .oils-box{position:absolute;left:16px;right:16px;top:302px;height:44px;
    border:1.5px solid var(--lime);display:flex;align-items:center;justify-content:center;
    font-weight:700;font-size:15px;line-height:15px}
  .label--plum .oils-box{color:var(--lime)}
  .blend{position:absolute;left:0;right:0;top:350px;font-weight:700;font-size:11.5px;line-height:12px}
  .label--leaf .blend{top:366px}
  .formula{position:absolute;left:0;right:0;top:392px;font-size:7px;font-weight:500;color:var(--lime)}
  .size{position:absolute;left:0;right:0;top:410px;font-size:7.5px;font-weight:500}
  .yield{position:absolute;left:0;right:0;top:420px;font-size:9px;font-weight:700}
  .back{padding:20px 14px 0}
  .back .tree-art{top:170px}
  .back-copy{position:relative;font-size:10.3px;line-height:11.6px;font-weight:500}
  .claims{position:relative;margin-top:14px;font-size:9.4px;line-height:11.4px;font-weight:500;color:var(--lime)}
  .claims + .claims{margin-top:10px}
  .ingredients{position:relative;margin-top:22px;font-size:8.6px;line-height:10.8px;font-weight:700}
  .guide{position:relative;margin-top:12px;font-size:8.6px;line-height:10.6px;font-weight:700}
  .warning{position:relative;margin-top:3px;font-size:7px;line-height:11px;font-weight:500}
</style>
</head>
<body>
<main class="sheet">

  <section class="label label--plum">
    <svg class="banner" viewBox="0 0 127 106" aria-hidden="true">
      <polygon points="0,0 127,0 127,80 63.5,106 0,80" fill="#fff"/>
      <polyline points="6,0 6,76 63.5,99 121,76 121,0" fill="none" stroke="#5c1a4a" stroke-width="1.5"/>
    </svg>
    <div class="brand-name">VOLDRIMO</div>
    <div class="tree-art" role="img" aria-label="Leafy tree with a joyful figure as its trunk"></div>
    <h1 class="title">AROMATHERAPY<br>CLEANING<br>CONCENTRATE</h1>
    <div class="oils-box">CONTAINS POWERFUL<br>ESSENTIAL OILS</div>
    <p class="blend">CINNAMON + CLOVE + LEMON<br>+ ROSEMARY + PEPPERMINT<br>+ EUCCALYPTUS</p>
    <p class="formula">ULTRA-CONCENTRATED VERSATILE FOMRULA</p>
    <p class="size">64 oz.</p>
    <p class="yield">MAKES UP TO 24 GALLONS OF CLEANER</p>
  </section>

  <section class="label label--plum back">
    <div class="tree-art" role="img" aria-label="Faint leafy tree with a joyful figure"></div>
    <p class="back-copy">Turn the mundane task of cleaning into an Aromatherapy Session while breezing through the house. From kitchen to bath to windows, doors and floors, this all-purpose NATURAL cleaner covers all. Our Potent essential oil enriched blend is safe to use in various ratios for virtually any cleaning task in you home. We unconditionally guarantee your sensory and cleaning Satisfaction. More at voldrimo.com</p>
    <p class="claims">YES<br>• Non Toxic • Family &amp; Earth Friendly<br>• Plant Based • Natural Ingredients<br>• Multi-purpose</p>
    <p class="claims">NO<br>• Laurel Sulfates • Preservatives<br>• Phthalates • Dyes • Synthetic Fragrance<br>• Vinegar • Chemical Concoctions</p>
    <p class="ingredients">Ingredients: Water, Essential Oils: Cinnamon Leaf (cinnamomum zeylanicum), Clove (eugenia caryoPhyllata), Lemon (citrus limonum), Eucalyptus Globulus, Rosemary (rosemarinus officianales), Peppermint (mentha piperita), Sodium Cocoate, Vegetable Glycerine, Sodium Chloride, Sodium Gluconate, Citric Acid.</p>
    <p class="guide">Visit voldrimo.com for complete use and difution guide.</p>
    <p class="warning">Keep out of reach of children. Stop use if irritation occurs. Keep out of eyes. For external use only.</p>
  </section>

  <section class="label label--leaf">
    <svg class="banner" viewBox="0 0 127 106" aria-hidden="true">
      <polygon points="0,0 127,0 127,80 63.5,106 0,80" fill="#fff"/>
      <polyline points="6,0 6,76 63.5,99 121,76 121,0" fill="none" stroke="#5cb84c" stroke-width="1.5"/>
    </svg>
    <div class="brand-name">VOLDRIMO</div>
    <div class="tree-art" role="img" aria-label="Leafy tree with a joyful figure as its trunk"></div>
    <h1 class="title">AROMATHERAPY<br>CLEANING<br>CONCENTRATE</h1>
    <div class="oils-box">CONTAINS POWERFUL<br>ESSENTIAL OILS</div>
    <p class="blend">LEMON+ROSEMARY</p>
    <p class="formula">ULTRA-CONCENTRATED VERSATILE FOMRULA</p>
    <p class="size">64 oz.</p>
    <p class="yield">MAKES UP TO 24 GALLONS OF CLEANER</p>
  </section>

</main>
</body>
</html>
```